Natural Light/Organic/Documentary Photography Business

I like a simple, approachable, feminine, earthy/organic feel. Earth/neutral tones, nothing too loud or obnoxious. I like the watercolor look. I don't want anything too trendy or something I'll get tired of after a couple months. As far as colors, I am much more a fan of cream/taupe/blue/green...not a fan of pink or purple at all.

Target Market(s)

Weddings & Families

Industry/Entity Type

Wedding Photography

Contact Information for Business Card

website, email, phone number

Font styles to use
Other font styles liked:
• Horizontes, Gotham

Colors

Designer to choose colors to be used in the design.

Requirements
Must have
• Website: www.meliskaverholt.com
• Phone: 482.319.6047
• Email: tessa@meliskaverholt.com
Nice to have
• I like the watercolor look but its not necessary. I like simple/earthy tones. Nothing too loud or distracting. Simple & feminine without being too girly. I like an approachable/soft feel.
• Instagram: www.instagram.com/meliskaverholtphotography/
Should not have
• NO loud colors or design or pattern. I do not want a photo of a camera or lens or anything cheesy like that.

```html
<!DOCTYPE html>
<html lang="en">
<head>
<meta charset="utf-8">
<title>Meliska Verholt Photography – Business Card</title>
<link rel="stylesheet" href="https://fonts.googleapis.com/css2?family=Montserrat:wght@300;400&display=swap">
<style>
  :root {
    --page: #ffffff;
    --card-white: #ffffff;
    --card-edge: #6f706b;
    --band: #7a7b75;
    --name: #6a6b66;
    --phone: #9c9d97;
    --contact: #dcdcd7;
    --mark-light: #efe6e1;
    --mark-warm: #e2cfc6;
  }
  * { margin: 0; padding: 0; box-sizing: border-box; }
  html, body {
    width: 1200px;
    height: 1200px;
    overflow: hidden;
    background: var(--page);
    font-family: "Montserrat", "Helvetica Neue", Arial, sans-serif;
  }
  .card {
    position: absolute;
    left: 24px;
    top: 276px;
    width: 1122px;
    height: 621px;
    background: var(--card-white);
    border: 1px solid var(--card-edge);
    overflow: hidden;
  }
  .card__band {
    position: absolute;
    left: 0;
    top: 276px;
    width: 100%;
    height: 345px;
    background: var(--band);
  }
  .card__monogram-area {
    position: absolute;
    left: 0;
    top: 268px;
    width: 482px;
    height: 168px;
    background: linear-gradient(100deg, var(--mark-light) 0%, var(--mark-warm) 55%, var(--mark-light) 100%);
    opacity: 0.55;
    border-radius: 0 0 90px 0;
  }
  .brand {
    position: absolute;
    left: 360px;
    top: 130px;
    width: 760px;
    text-align: center;
  }
  .brand__name {
    font-weight: 300;
    font-size: 66px;
    letter-spacing: 2px;
    color: var(--name);
    line-height: 1;
  }
  .brand__tagline {
    margin-top: 18px;
    font-weight: 400;
    font-size: 16px;
    letter-spacing: 9px;
    color: var(--name);
    padding-left: 9px;
  }
  .contact {
    position: absolute;
    left: 380px;
    top: 368px;
    width: 646px;
    text-align: center;
    font-weight: 300;
  }
  .contact__phone {
    font-size: 42px;
    letter-spacing: 2px;
    color: var(--phone);
    line-height: 1;
  }
  .contact__web,
  .contact__email {
    font-size: 38px;
    color: var(--contact);
    line-height: 1;
    letter-spacing: 0.5px;
  }
  .contact__web { margin-top: 40px; }
  .contact__email { margin-top: 14px; }
</style>
</head>
<body>
  <div class="card">
    <div class="card__band"></div>
    <div class="card__monogram-area" role="img" aria-label="Large soft watercolour monogram decoration in blush and cream tones"></div>

    <div class="brand">
      <div class="brand__name">Meliska Verholt</div>
      <div class="brand__tagline">PHOTOGRAPHY</div>
    </div>

    <div class="contact">
      <div class="contact__phone">482.319.6047</div>
      <div class="contact__web">www.meliskaverholt.com</div>
      <div class="contact__email">tessa@meliskaverholt.com</div>
    </div>
  </div>
</body>
</html>
```